Generic Business Card

I need a business card for my new cafe which is only six weeks old. I'm continuously asked for a business so that customers can either keep or pass on to a friend. I'd also like a card that I can give out with each bill which contains the business name, address, contact details and website.
The cafe's internal design has an industrial feel to it with modern subdued colours. I have attached an internal photo along with my main hero shot and logo.
The hero shot features prominently on my website and other print material and I would also like it to appear on my bus card.

Target Market(s)

Men & women between 35 and 45 years of age who know and enjoy good coffee.

Industry/Entity Type

Industrial

Contact Information for Business Card

Shop 7b/318-320 Pellmore Road, East Caldervale 3187
Tel. 9642 3715
www.tolvana.com.au

```html
<!DOCTYPE html>
<html lang="en">
<head>
<meta charset="utf-8">
<title>Tolvana – Business Card</title>
<link rel="stylesheet" href="https://fonts.googleapis.com/css2?family=PT+Sans:wght@400;700&display=swap">
<style>
  :root {
    --page-bg: #ececec;
    --ink: #1c1912;
    --panel-dark: #14110d;
    --text-light: #f4f1e8;
    --accent-yellow: #f2c81e;
    --frame-line: rgba(255, 255, 255, 0.85);
  }
  * { box-sizing: border-box; margin: 0; padding: 0; }
  html, body {
    width: 1200px;
    height: 800px;
    overflow: hidden;
    background: var(--page-bg);
    font-family: "PT Sans", Arial, sans-serif;
  }
  .business-card {
    position: absolute;
    left: 120px;
    top: 100px;
    width: 960px;
    height: 600px;
    overflow: hidden;
    box-shadow: 0 6px 20px rgba(0, 0, 0, 0.18);
  }
  .cafe-interior-photo {
    position: absolute;
    inset: 0;
    background:
      linear-gradient(180deg, rgba(0,0,0,0) 45%, rgba(40,26,12,0.75) 100%),
      linear-gradient(90deg, #eee22c 0%, #d9d12a 38%, #4a4a2c 44%, #6f8062 62%, #6b7a5c 80%, #3d3a22 100%);
  }
  .card-frame {
    position: absolute;
    left: 19px;
    top: 24px;
    width: 922px;
    height: 552px;
    border: 2px solid var(--frame-line);
  }
  .corner-block {
    position: absolute;
    background: var(--panel-dark);
  }
  .corner-block--top-left { left: 0; top: 0; width: 211px; height: 36px; }
  .corner-block--bottom-right { right: 0; bottom: 0; width: 221px; height: 43px; }
  .brand {
    position: absolute;
    left: 43px;
    top: 86px;
    color: var(--ink);
  }
  .brand-name {
    font-size: 90px;
    font-weight: 700;
    letter-spacing: 4px;
    line-height: 1;
  }
  .brand-tagline {
    margin-top: 6px;
    text-align: right;
    font-size: 30px;
    font-weight: 700;
  }
  .website-bar {
    position: absolute;
    left: 36px;
    top: 490px;
    width: 353px;
    height: 57px;
    background: var(--panel-dark);
    color: var(--text-light);
    font-size: 27px;
    line-height: 57px;
    text-align: center;
  }
  .contact-list {
    position: absolute;
    left: 470px;
    top: 350px;
    list-style: none;
    color: var(--text-light);
    font-size: 29px;
    line-height: 37px;
  }
  .contact-item {
    display: flex;
    align-items: flex-start;
    gap: 16px;
  }
  .contact-item + .contact-item { margin-top: 26px; }
  .contact-icon {
    flex: none;
    width: 34px;
    height: 34px;
    margin-top: 2px;
  }
</style>
</head>
<body>
  <div class="business-card">
    <div class="cafe-interior-photo" role="img" aria-label="Cafe interior photo: yellow wall, long wooden table and chairs"></div>
    <div class="corner-block corner-block--top-left"></div>
    <div class="corner-block corner-block--bottom-right"></div>
    <div class="card-frame"></div>

    <div class="brand">
      <div class="brand-name">TOLVANA</div>
      <div class="brand-tagline">eat &amp; drink</div>
    </div>

    <div class="website-bar">www.tolvana.com.au</div>

    <ul class="contact-list">
      <li class="contact-item">
        <svg class="contact-icon" viewBox="0 0 34 34" aria-hidden="true">
          <rect width="34" height="34" rx="7" fill="var(--accent-yellow)"/>
          <path d="M11 9c1.5 0 3 3 3 4s-1.5 1.5-1.5 2.5 3 5 6 6c1 0 1.5-1.5 2.5-1.5s4 1.5 4 3-2 3-3.5 3C15 26 8 19 8 12.5 8 11 9.5 9 11 9z" fill="var(--panel-dark)"/>
        </svg>
        <span>9642 3715</span>
      </li>
      <li class="contact-item">
        <svg class="contact-icon" viewBox="0 0 34 34" aria-hidden="true">
          <rect width="34" height="34" rx="7" fill="var(--accent-yellow)"/>
          <path d="M17 6a7.5 7.5 0 0 0-7.5 7.5C9.5 19 17 28 17 28s7.5-9 7.5-14.5A7.5 7.5 0 0 0 17 6z" fill="var(--text-light)"/>
          <circle cx="17" cy="13.5" r="3" fill="var(--accent-yellow)"/>
        </svg>
        <span>Shop 7b/318-320<br>Pellmore Road,<br>East Caldervale 3187</span>
      </li>
    </ul>
  </div>
</body>
</html>
```